Business Card for my New Brokerage

Looking to get a business card design for my new Real Estate Brokerage.
I want it with Picture, Phone Number, Email, Website, Office Address
Name and Designation. Please add logo too.

Target Market(s)

Real Estate Investors or Home Buyers

Industry/Entity Type

Real Estate

Contact Information for Business Card

Name, Email, Phone Number, website, email, office address

Colors
EB3D1F
EC4F4E
F09395
F8D3D4
FCEDEE

Requirements
Must have
• Minimalistic, Clean, Modern, Photo
Nice to have
• White and Red Colors

```html
<!DOCTYPE html>
<html lang="en">
<head>
<meta charset="utf-8">
<title>Ember Realty Co — Business Card</title>
<link href="https://fonts.googleapis.com/css2?family=Montserrat:wght@400;500;600;700&display=swap" rel="stylesheet">
<style>
  :root {
    --brand-red: #dd0000;
    --paper: #ffffff;
    --ink: #555555;
    --backdrop: #1e1e1e;
    --silver: #cfcfcf;
    --photo-tone-a: #d9dde3;
    --photo-tone-b: #2b3240;
  }
  * { box-sizing: border-box; margin: 0; padding: 0; }
  html, body {
    width: 1200px; height: 1199px; overflow: hidden;
    background: var(--backdrop);
    font-family: "Montserrat", sans-serif;
  }
  .card {
    position: absolute;
    left: 195px;
    width: 800px;
    height: 435px;
    overflow: hidden;
  }
  .card--front { top: 115px; background: var(--paper); }
  .card--back { top: 650px; background: var(--brand-red); }

  .brand-name {
    position: absolute;
    left: 52px; top: 52px;
    color: var(--brand-red);
    font-weight: 600;
    text-transform: uppercase;
    line-height: 1;
  }
  .brand-name__main {
    display: block;
    font-size: 56px;
    letter-spacing: 1px;
  }
  .brand-name__sub {
    display: block;
    margin-top: 10px;
    padding-left: 52px;
    font-size: 17px;
    letter-spacing: 4.5px;
  }

  .name-band {
    position: absolute;
    left: 0; top: 167px;
    width: 100%; height: 113px;
    background: var(--brand-red);
  }
  .agent-name {
    position: absolute;
    left: 52px; top: 192px;
    color: var(--paper);
    font-weight: 600;
    font-size: 34px;
    letter-spacing: 1px;
    line-height: 1.1;
    text-transform: uppercase;
  }
  .agent-title {
    position: absolute;
    left: 52px; top: 232px;
    color: var(--paper);
    font-weight: 500;
    font-size: 20px;
    letter-spacing: 0.5px;
  }

  .agent-photo {
    position: absolute;
    left: 538px; top: 122px;
    width: 208px; height: 204px;
    border-radius: 50%;
    border: 2px solid var(--brand-red);
    background: var(--paper);
    padding: 3px;
  }
  .agent-photo span {
    display: block; width: 100%; height: 100%;
    border-radius: 50%;
    background: linear-gradient(180deg, var(--photo-tone-a) 0%, var(--photo-tone-a) 45%, var(--photo-tone-b) 100%);
  }

  .contact-list {
    position: absolute;
    left: 52px; top: 324px;
    list-style: none;
    color: var(--ink);
    font-size: 19.5px;
    letter-spacing: 0.3px;
  }
  .contact-list li {
    display: flex; align-items: center; gap: 8px;
    height: 26px;
  }
  .contact-list svg { width: 14px; height: 14px; flex: none; }

  .office-address {
    position: absolute;
    right: 53px; top: 350px;
    text-align: right;
    color: var(--ink);
    font-size: 19.5px;
    letter-spacing: 0.3px;
    font-style: normal;
    line-height: 26px;
  }

  .brand-name--large {
    position: absolute;
    left: 0; right: 0; top: 172px;
    text-align: center;
    color: var(--silver);
    font-weight: 600;
    text-transform: uppercase;
    line-height: 1;
  }
  .brand-name--large .brand-name__main {
    font-size: 112px;
    letter-spacing: 2px;
  }
  .brand-name--large .brand-name__sub {
    margin-top: 18px;
    padding-left: 0;
    font-size: 33px;
    letter-spacing: 9px;
  }
</style>
</head>
<body>
  <section class="card card--front">
    <div class="brand-name">
      <span class="brand-name__main">Ember</span>
      <span class="brand-name__sub">Realty Co</span>
    </div>

    <div class="name-band"></div>
    <h1 class="agent-name">Daniel Hart</h1>
    <p class="agent-title">Founder and President</p>

    <div class="agent-photo"><span role="img" aria-label="Portrait photo of the agent"></span></div>

    <ul class="contact-list">
      <li>
        <svg viewBox="0 0 24 24" fill="var(--brand-red)"><path d="M6.6 10.8a15 15 0 0 0 6.6 6.6l2.2-2.2c.3-.3.7-.4 1-.2 1.1.4 2.3.6 3.6.6.6 0 1 .4 1 1V20c0 .6-.4 1-1 1A17 17 0 0 1 3 4c0-.6.4-1 1-1h3.5c.6 0 1 .4 1 1 0 1.2.2 2.4.6 3.6.1.3 0 .7-.2 1z"/></svg>
        +1 478-555-0192
      </li>
      <li>
        <svg viewBox="0 0 24 24" fill="none" stroke="var(--brand-red)" stroke-width="2.5"><rect x="2" y="5" width="20" height="14" rx="2"/><path d="M2 7l10 7 10-7"/></svg>
        info@emberrealtyco.com
      </li>
      <li>
        <svg viewBox="0 0 24 24" fill="none" stroke="var(--brand-red)" stroke-width="2"><circle cx="12" cy="12" r="10"/><ellipse cx="12" cy="12" rx="4" ry="10"/><path d="M2 12h20M4 7h16M4 17h16"/></svg>
        www.emberrealtyco.com
      </li>
    </ul>

    <address class="office-address">1870 Cedar Ridge Way<br>Maple Grove, GA 31000</address>
  </section>

  <section class="card card--back">
    <div class="brand-name--large">
      <span class="brand-name__main">Ember</span>
      <span class="brand-name__sub">Realty Co</span>
    </div>
  </section>
</body>
</html>
```